Water Filter Company Needs Bizz Cards!!

Need business cards for my company. We sell whole home water filters and salt free water softeners. No more buying bottled water. Our filtering units filter out all heavy metals, chlorine, and VOC's, last 15 years, and are maintenance free and supply your whole home with spring quality alkaline water. Our Salt free water conditioners, eliminate hard water and scale, without lowering the ph, or TDS's (total Dissolved solids)

I think this is the color code we are using on my site. My logo looks good behind it. #192841

Website will be www.Brovexa.com

Industry/Entity Type

Water Purification

Contact Information for Business Card

For now, just insert standard Dummy text. I need these text lines for the info to be editable so i can make them for multiple employees. I do have Photoshop and illustrator, unless there is a simpler program i can use solely for biz cards

Font styles to use
Sans Serif

Requirements
Must have
• Use my preexisting logo.

www.BroVexa.com

Spring Quality Alkaline Water at every tap.

List out services. Whole Home Water Filters, Salt Free Water Softeners, Clarimont KT7, UV Sterilizers
Nice to have
• I think this is the color code we are using on my site. My logo looks good behind it. #192841 or black. Please no white or light blue backgrounds.

Maybe a picture of my tank.

Slogan like Spring Quality Alkaline Water at every tap.
And just list the services Whole Home Water Filters, Salt Free Water Softeners, Clarimont KT7, UV Sterilizers

I think I would like to not have a contrasting textured logo like I see on some of them. I may use it for my personal cards, but new employees may not want the extra expense.
Should not have
• A different logo than the one provided.

White or baby blue backgrounds. Use the color code, or blacks.

```html
<!DOCTYPE html>
<html lang="en">
<head>
<meta charset="utf-8">
<title>BroVexa Business Cards</title>
<link href="https://fonts.googleapis.com/css2?family=Montserrat:wght@400;500;600;700;800&family=Teko:wght@500&display=swap" rel="stylesheet">
<style>
  :root {
    --page: #d4d4d4;
    --navy: #192841;
    --navy-light: #21365a;
    --sky: #3ec0ee;
    --ice: #a9d8ee;
    --text: #dfe5ee;
    --tank: #161616;
  }
  * { box-sizing: border-box; margin: 0; padding: 0; }
  html, body { width: 1200px; height: 800px; overflow: hidden; }
  body {
    background: var(--page);
    font-family: "Montserrat", sans-serif;
    position: relative;
  }
  .card {
    position: absolute;
    top: 284px;
    width: 430px;
    height: 239px;
    background: radial-gradient(ellipse at 45% 35%, var(--navy-light) 0%, var(--navy) 70%);
    overflow: hidden;
    color: var(--text);
  }
  .card--front { left: 110px; }
  .card--back { left: 638px; }

  .brand-name {
    font-family: "Montserrat", sans-serif;
    font-weight: 700;
    color: var(--sky);
    letter-spacing: -0.5px;
    line-height: 1;
  }
  .card--front .brand-name {
    position: absolute; left: 16px; top: 18px; font-size: 34px;
  }
  .contact-name {
    position: absolute; left: 14px; top: 84px;
    border-left: 3px solid var(--sky);
    padding-left: 9px;
  }
  .contact-name h1 {
    font-size: 19px; font-weight: 600; color: var(--sky);
    letter-spacing: 0.3px; line-height: 1.1;
  }
  .contact-name p { font-size: 11px; font-weight: 400; margin-top: 1px; }

  .contact-list {
    position: absolute; left: 12px; top: 128px;
    list-style: none; font-size: 11px; line-height: 13.5px;
  }
  .contact-list li { display: flex; align-items: flex-start; gap: 6px; }
  .contact-list li.gap { margin-bottom: 7px; }
  .contact-list svg { width: 11px; height: 11px; flex: none; margin-top: 1px; }

  .slogan {
    position: absolute; left: 0; top: 212px;
    border-left: 3px solid var(--sky);
    padding-left: 11px;
    font-family: "Teko", sans-serif; font-weight: 500;
    font-size: 16px; line-height: 14px; color: var(--sky);
    text-transform: uppercase; letter-spacing: 0.1px;
  }
  .accent-glow {
    position: absolute; right: -60px; top: 20px;
    width: 220px; height: 220px; border-radius: 50%;
    background: radial-gradient(circle, rgba(62,192,238,0.18) 0%, rgba(62,192,238,0) 70%);
  }
  .accent-glow--back { left: -80px; right: auto; }

  .back-brand {
    position: absolute; left: 97px; top: 86px;
    display: flex; align-items: center; gap: 10px;
  }
  .back-brand .dot {
    width: 18px; height: 18px; border-radius: 50%; background: var(--sky);
  }
  .back-brand .brand-name { font-size: 46px; }

  .services {
    position: absolute; left: 97px; top: 169px;
    list-style: none;
    font-size: 11px; font-weight: 700; letter-spacing: 0.9px;
    line-height: 13.2px; text-transform: uppercase;
  }
  .services li { display: flex; align-items: center; gap: 6px; }
  .services li::before {
    content: ""; width: 5px; height: 5px; border-radius: 50%; background: var(--sky);
  }

  .tank-photo {
    position: absolute; left: 381px; top: 14px;
    width: 46px; height: 222px; border-radius: 6px;
    background: linear-gradient(90deg, #0c0c0c 0%, #2c2c2c 45%, #111 100%);
  }
</style>
</head>
<body>
  <section class="card card--front">
    <div class="accent-glow"></div>
    <div class="brand-name">BroVexa</div>
    <div class="contact-name">
      <h1>MARCUS DELANEY</h1>
      <p>CEO/ Owner</p>
    </div>
    <ul class="contact-list">
      <li class="gap">
        <svg viewBox="0 0 12 12"><path d="M6 1a3.5 3.5 0 0 0-3.5 3.5C2.5 7.3 6 11 6 11s3.5-3.7 3.5-6.5A3.5 3.5 0 0 0 6 1z" fill="none" stroke="#3ec0ee" stroke-width="1"/><circle cx="6" cy="4.5" r="1.2" fill="none" stroke="#3ec0ee"/></svg>
        <span>4820 Fenwick Avenue<br>Harlow Springs, USA</span>
      </li>
      <li>
        <svg viewBox="0 0 12 12"><path d="M3 1.5l1.5 2-1 1.2c.7 1.5 1.8 2.6 3.3 3.3l1.2-1 2 1.5-.8 1.8C6 10 2 6 1.7 2.3z" fill="none" stroke="#3ec0ee" stroke-width="1"/></svg>
        <span>(555) 0142 386 207</span>
      </li>
      <li>
        <svg viewBox="0 0 12 12"><rect x="1" y="2.5" width="10" height="7" fill="none" stroke="#3ec0ee"/><path d="M1 2.5l5 4 5-4" fill="none" stroke="#3ec0ee"/></svg>
        <span>hello@brovexa.com</span>
      </li>
      <li>
        <svg viewBox="0 0 12 12"><circle cx="6" cy="6" r="5" fill="none" stroke="#3ec0ee"/><path d="M1 6h10M6 1c-2 2.5-2 7.5 0 10M6 1c2 2.5 2 7.5 0 10" fill="none" stroke="#3ec0ee" stroke-width="0.8"/></svg>
        <span>www.BroVexa.com</span>
      </li>
    </ul>
    <p class="slogan">Spring quality alkaline water at every tap</p>
  </section>

  <section class="card card--back">
    <div class="accent-glow accent-glow--back"></div>
    <div class="back-brand">
      <span class="dot"></span>
      <span class="brand-name">BroVexa</span>
    </div>
    <ul class="services">
      <li>Whole Home Water Filters</li>
      <li>Salt Free Water Softeners</li>
      <li>Clarimont KT7</li>
      <li>UV Sterilizers</li>
    </ul>
    <div class="tank-photo" role="img" aria-label="Photo of the black whole home water filter tank with control valve"></div>
  </section>
</body>
</html>
```